Business Cards and Logo needed for Rum Website

I need a smart, modern but fun business card (and Logo) to help promote my website BrightBarrelNote.com

The website contains reviews of Rum (and eventually other spirits) as well as news and blog posts.

I would like a 2-sided design, with the logo and company name on one side and text on the other.

Text fields required are:
Name (Dan Wheeler)
Website (www.brightbarrelnote.com)
Email (dan@brightbarrelnote.com)
Twitter (@BrightBarrelNote)

For the logo i'm open to suggestions however it must incorporate a wooden Cask and a number of Stars. Ideas so far have been for a Cask surrounded in a number of Stars forming a circle around it with the text Bright Barrel Note underneath. The logo should be modern but also a little bit cartoony and stylised. General drink/spirits themes will also be considered.

Colours: I like the idea of yellow text with black background but again i'm open to suggestions on what would work well. Contrasting colours for the 2-sides would be good.

Cards will be printed via Printlo.com so please consult their style guidelines if required: http://uk.printlo.com/help/faq/templates-and-guidelines.html

Requirements
Must have
• A spirits Cask
A number of Stars (preferrably yellow or gold)

```html
<!DOCTYPE html>
<html lang="en">
<head>
<meta charset="utf-8">
<title>Bright Barrel Note – Business Cards</title>
<link rel="stylesheet" href="https://fonts.googleapis.com/css2?family=Oswald:wght@600&family=Open+Sans:wght@600;700&display=swap">
<style>
  :root {
    --backdrop: #3b3b3b;
    --orange: #ee7d1f;
    --orange-light: #f9b04c;
    --orange-deep: #e2691a;
    --brown: #6b3a1c;
    --cream: #fbeadb;
    --white: #ffffff;
  }
  * { margin: 0; padding: 0; box-sizing: border-box; }
  html, body {
    width: 1200px; height: 874px; overflow: hidden;
    background: var(--backdrop);
  }
  .card-set { position: relative; width: 1200px; height: 874px; }
  .card {
    position: absolute; top: 267px;
    width: 520px; height: 340px;
    overflow: hidden;
    box-shadow: 0 14px 30px rgba(0,0,0,.45);
  }

  /* Front side */
  .card-front {
    left: 50px;
    background: radial-gradient(ellipse at 35% 45%, var(--orange-light) 0%, var(--orange) 55%, var(--orange-deep) 100%);
  }
  .front-lockup {
    position: absolute; left: 50%; top: 50%;
    transform: translate(-50%, -50%) rotate(-28deg);
    display: flex; flex-direction: column; align-items: flex-end;
    white-space: nowrap;
  }
  .front-brand {
    display: flex; align-items: center; gap: 12px;
  }
  .brand-dot {
    width: 24px; height: 24px; border-radius: 50%;
    background: var(--white); flex: none;
  }
  .front-brand .brand-name {
    font-family: "Oswald", sans-serif; font-weight: 600;
    font-size: 42px; letter-spacing: 1px; line-height: 1;
    color: var(--white); text-transform: uppercase;
  }
  .front-url {
    margin-top: 8px;
    font-family: "Open Sans", sans-serif; font-weight: 700;
    font-size: 14px; letter-spacing: 1.5px; color: var(--brown);
  }

  /* Back side */
  .card-back { left: 630px; background: var(--white); }
  .back-brand {
    position: absolute; left: 28px; top: 30px;
    font-family: "Oswald", sans-serif; font-weight: 600;
    font-size: 24px; letter-spacing: .5px; line-height: 1.2;
    color: var(--orange); text-transform: uppercase;
  }
  .back-watermark {
    position: absolute; left: 28px; top: 78px;
    font-family: "Oswald", sans-serif; font-weight: 600;
    font-size: 48px; line-height: 1.1; white-space: nowrap;
    color: var(--cream); text-transform: uppercase;
  }
  .contact {
    position: absolute; left: 28px; top: 170px;
    font-family: "Open Sans", sans-serif;
  }
  .contact-name {
    font-weight: 700; font-size: 19px; letter-spacing: 3px;
    color: var(--brown); text-transform: uppercase;
    margin-bottom: 8px;
  }
  .contact-line {
    font-weight: 700; font-size: 13px; line-height: 22px;
    letter-spacing: .6px;
  }
  .contact-label { color: var(--brown); }
  .contact-value { color: var(--orange); }
  .back-band {
    position: absolute; left: 0; right: 0; bottom: 0; height: 16px;
    background: var(--orange);
  }
</style>
</head>
<body>
  <main class="card-set">
    <section class="card card-front" aria-label="Card front">
      <div class="front-lockup">
        <div class="front-brand">
          <span class="brand-dot"></span>
          <span class="brand-name">Bright Barrel Note</span>
        </div>
        <p class="front-url">www.brightbarrelnote.com</p>
      </div>
    </section>

    <section class="card card-back" aria-label="Card back">
      <div class="back-brand">Bright Barrel Note</div>
      <div class="back-watermark" aria-hidden="true">Bright Barrel Note</div>
      <div class="contact">
        <p class="contact-name">Dan Wheeler</p>
        <p class="contact-line"><span class="contact-label">email:</span> <span class="contact-value">dan@brightbarrelnote.com</span></p>
        <p class="contact-line"><span class="contact-label">twitter:</span> <span class="contact-value">@BrightBarrelNote</span></p>
        <p class="contact-line"><span class="contact-label">website:</span> <span class="contact-value">www.brightbarrelnote.com</span></p>
      </div>
      <div class="back-band"></div>
    </section>
  </main>
</body>
</html>
```